Real Estate Sales & Property Management Company Business Cards
Harwell Estates New Business Card Design
Real Estate Sales & Property Management Company Business Cards -
Creative Brief
Professional
Maribel J. Olstad
Broker/President
4175 Bramble Ct. Suite 27 Carmichael, CA 95731
916-555-0148 ext.217
maribel@harwell-estates.example
www.harwell-estates.example
"The Only Place to be for your real estate needs." Real Estate Sales/Aquisitions Professional Property Management Market Analysis 1031 Exchanges Tenant Screening/Leasing Only Services Investment Property Consultation Rental Property Rehab/Maintenance

```html
<!DOCTYPE html>
<html lang="en">
<head>
<meta charset="utf-8">
<title>Harwell Estates Stationery</title>
<link href="https://fonts.googleapis.com/css2?family=Cormorant+Garamond:wght@600&family=Open+Sans:wght@400;600&display=swap" rel="stylesheet">
<style>
  :root {
    --navy: #18237a;
    --blue: #2a45c4;
    --blue-light: #4d6ae0;
    --ink: #3a3f4a;
    --grey-band: #8a8d93;
    --orb: #c9ccd3;
    --paper: #ffffff;
    --stage: #ffffff;
    --line: #d6d8dc;
    --black-card: #0d0d12;
  }
  * { margin: 0; padding: 0; box-sizing: border-box; }
  html, body { width: 1200px; height: 584px; overflow: hidden; background: var(--stage); }
  body { position: relative; font-family: "Open Sans", Arial, sans-serif; color: var(--ink); }

  .sheet { position: absolute; background: var(--paper); border: 1px solid var(--line); overflow: hidden; }

  .wordmark { font-family: "Cormorant Garamond", Georgia, serif; font-weight: 600; color: var(--navy);
    text-align: center; line-height: 1; letter-spacing: 1px; text-transform: uppercase; }
  .wordmark .dot { display: block; margin: 0 auto 3px; border-radius: 50%; background: var(--navy); }
  .wordmark.on-dark { color: #fff; }
  .wordmark.on-dark .dot { background: #fff; }

  .orb { position: absolute; border-radius: 50%;
    background: radial-gradient(circle at 40% 40%, #f1f2f5 0%, var(--orb) 70%, #b5b9c2 100%); opacity: .7; }

  .band { position: absolute; left: 0; right: 0;
    background: linear-gradient(90deg, var(--navy) 0%, var(--blue) 50%, var(--blue-light) 100%); }

  .tiny { font-size: 5.5px; line-height: 1.5; }

  /* letterhead */
  .letterhead { left: 24px; top: 12px; width: 360px; height: 498px; }
  .letterhead .band.top { top: 0; height: 36px; }
  .letterhead .wordmark { position: absolute; top: 4px; left: 0; right: 0; font-size: 13px; }
  .letterhead .wordmark .dot { width: 10px; height: 10px; }
  .letterhead .band.bottom { bottom: 0; height: 42px; color: #fff; text-align: center; padding-top: 10px; }

  /* envelope */
  .envelope { left: 391px; top: 12px; width: 377px; height: 216px; }
  .envelope .flap { position: absolute; top: 0; left: 0; right: 0; height: 24px; background: var(--grey-band); }
  .envelope .wordmark { position: absolute; top: 26px; left: 0; right: 0; font-size: 12px; }
  .envelope .wordmark .dot { width: 10px; height: 10px; }
  .envelope .address { position: absolute; top: 128px; left: 0; right: 0; text-align: center; }

  /* window envelope */
  .mailer { left: 391px; top: 240px; width: 377px; height: 143px; }
  .mailer .wordmark { position: absolute; left: 10px; top: 52px; font-size: 11px; text-align: left; }
  .mailer .wordmark .dot { width: 9px; height: 9px; margin: 0 0 3px 14px; }
  .mailer .sender { position: absolute; left: 10px; top: 98px; }
  .mailer .recipient { position: absolute; right: 14px; top: 100px; }

  /* business cards */
  .card { position: absolute; width: 148px; height: 86px; overflow: hidden; border: 1px solid var(--line); }
  .card-front { background: var(--paper); }
  .card-front .wordmark { position: absolute; left: 6px; top: 12px; font-size: 8px; }
  .card-front .wordmark .dot { width: 8px; height: 8px; }
  .card-front .person { position: absolute; left: 62px; top: 12px; border-left: 1px solid var(--line); padding-left: 5px; }
  .card-front .person .name { font-size: 7px; font-weight: 600; color: var(--navy); }
  .card-front .band { bottom: 0; height: 30px; color: #fff; padding: 3px 6px; white-space: nowrap; }
  .card-back { color: #fff; text-align: center; padding: 8px 8px; }
  .card-back.blue { background: linear-gradient(135deg, var(--navy), var(--blue) 60%, var(--blue-light)); }
  .card-back.black { background: var(--black-card); }
  .card-back .tagline { font-style: italic; font-size: 5.5px; margin-bottom: 4px; }
  .card-back ul { list-style: none; font-size: 5px; line-height: 1.45; }

  .card-b-front { left: 427px; top: 478px; }
  .card-b-front .wordmark { left: 0; right: 0; top: 6px; }
  .card-b-front .person { left: auto; right: 6px; top: 32px; border: 0; text-align: right; }

  /* second page */
  .second-sheet { left: 816px; top: 12px; width: 374px; height: 497px; }
  .second-sheet .wordmark { position: absolute; left: 10px; top: 12px; font-size: 15px; text-align: left; }
  .second-sheet .wordmark .dot { width: 12px; height: 12px; margin: 0 0 4px 24px; }
  .second-sheet .contact { position: absolute; left: 200px; top: 10px; border-left: 1px solid var(--navy); padding-left: 5px; }
  .second-sheet .rule { position: absolute; left: 0; right: 0; top: 58px; height: 3px; background: var(--navy); }
</style>
</head>
<body>

<section class="sheet letterhead">
  <div class="band top"></div>
  <div class="wordmark on-dark"><span class="dot"></span>Harwell Estates</div>
  <div class="orb" style="left:-90px;top:350px;width:200px;height:200px;"></div>
  <div class="band bottom tiny">
    <p>4175 Bramble Ct. Suite 27 Carmichael, CA 95731</p>
    <p>Phone: 916-555-0148 ext.217</p>
    <p>maribel@harwell-estates.example | www.harwell-estates.example</p>
  </div>
</section>

<section class="sheet envelope">
  <div class="flap"></div>
  <div class="wordmark"><span class="dot"></span>Harwell Estates</div>
  <div class="orb" style="right:-40px;top:80px;width:110px;height:110px;"></div>
  <div class="address tiny">
    <p>4175 Bramble Ct. Suite 27 Carmichael, CA 95731</p>
    <p>916-555-0148 ext.217</p>
    <p>www.harwell-estates.example</p>
  </div>
</section>

<section class="sheet mailer">
  <div class="orb" style="right:-30px;top:-40px;width:110px;height:110px;"></div>
  <div class="wordmark"><span class="dot"></span>Harwell<br>Estates</div>
  <div class="sender tiny">
    <p>4175 Bramble Ct. Suite 27</p>
    <p>Carmichael, CA 95731</p>
    <p>maribel@harwell-estates.example</p>
  </div>
  <p class="recipient tiny">Recipient Address</p>
</section>

<article class="card card-front" style="left:427px;top:389px;">
  <div class="wordmark"><span class="dot"></span>Harwell<br>Estates</div>
  <div class="person">
    <p class="name">Maribel J. Olstad</p>
    <p class="tiny">Broker/President</p>
  </div>
  <div class="band tiny">
    <p>4175 Bramble Ct. Suite 27 Carmichael, CA 95731</p>
    <p>916-555-0148 ext.217</p>
    <p>www.harwell-estates.example</p>
  </div>
</article>

<article class="card card-back blue" style="left:583px;top:389px;">
  <p class="tagline">"The Only Place to be for your real estate needs."</p>
  <ul>
    <li>Real Estate Sales/Aquisitions</li>
    <li>Professional Property Management</li>
    <li>Market Analysis · 1031 Exchanges</li>
    <li>Tenant Screening/Leasing Only Services</li>
    <li>Investment Property Consultation</li>
    <li>Rental Property Rehab/Maintenance</li>
  </ul>
</article>

<article class="card card-front card-b-front">
  <div class="wordmark"><span class="dot"></span>Harwell Estates</div>
  <div class="person">
    <p class="name">Maribel J. Olstad</p>
    <p class="tiny">Broker/President</p>
  </div>
  <div class="band tiny">
    <p>4175 Bramble Ct. Suite 27 Carmichael, CA 95731</p>
    <p>maribel@harwell-estates.example</p>
    <p>www.harwell-estates.example</p>
  </div>
</article>

<article class="card card-back black" style="left:583px;top:478px;">
  <p class="tagline">"The Only Place to be for your real estate needs."</p>
  <ul>
    <li>Real Estate Sales/Aquisitions</li>
    <li>Professional Property Management</li>
    <li>Market Analysis · 1031 Exchanges</li>
    <li>Tenant Screening/Leasing Only Services</li>
    <li>Investment Property Consultation</li>
    <li>Rental Property Rehab/Maintenance</li>
  </ul>
</article>

<section class="sheet second-sheet">
  <div class="wordmark"><span class="dot"></span>Harwell Estates</div>
  <div class="contact tiny">
    <p>4175 Bramble Ct. Suite 27</p>
    <p>Carmichael, CA 95731</p>
    <p>916-555-0148 ext.217</p>
    <p>maribel@harwell-estates.example</p>
    <p>www.harwell-estates.example</p>
  </div>
  <div class="rule"></div>
  <div class="orb" style="right:-80px;top:340px;width:180px;height:180px;"></div>
</section>

</body>
</html>
```